Brivora Collective Business Card Design

We need a business card design for Brivora Collective. We are a healthcare recruiting, wellness and education company. We partner with medical facilities to find quality candidates. We also offer free wellness courses.
The final design should communicate an emphasis on recruiting and wellness
The main purpose of the business card is to utilized it for networking events, give to hospitals, executives, VCs surgery centers and clinics. I want it to be sleek, clean, use of our brand colors and professional.

```html
<!DOCTYPE html>
<html lang="en">
<head>
<meta charset="utf-8">
<title>Brivora Collective Business Card</title>
<link href="https://fonts.googleapis.com/css2?family=Montserrat:wght@400;600;700&display=swap" rel="stylesheet">
<style>
  :root {
    --teal: #00695f;
    --teal-light: #007a70;
    --teal-dark: #00564e;
    --white: #ffffff;
    --paper: #f4f4f4;
    --backdrop: #2a2c2d;
  }
  html, body {
    margin: 0;
    padding: 0;
    width: 1200px;
    height: 1200px;
    overflow: hidden;
    background: var(--backdrop);
    font-family: "Montserrat", sans-serif;
  }
  .stage {
    position: relative;
    width: 1200px;
    height: 1200px;
  }
  .card {
    position: absolute;
    left: 250px;
    width: 700px;
    height: 400px;
    overflow: hidden;
    box-shadow: 0 18px 40px rgba(0,0,0,0.45);
  }
  .card-front {
    top: 130px;
    background: radial-gradient(circle at 45% 70%, var(--teal-light), var(--teal-dark) 90%);
    display: flex;
    align-items: center;
    justify-content: center;
  }
  .wordmark {
    display: flex;
    align-items: center;
    gap: 18px;
    font-weight: 600;
    font-size: 54px;
    letter-spacing: -0.5px;
    line-height: 1;
  }
  .wordmark-mark {
    width: 44px;
    height: 44px;
    border-radius: 8px;
    flex: none;
  }
  .card-front .wordmark { color: var(--white); }
  .card-front .wordmark-mark { background: var(--white); }

  .card-back {
    top: 630px;
    background: var(--paper);
  }
  .card-back .curve {
    position: absolute;
    inset: 0;
  }
  .contact {
    position: absolute;
    left: 48px;
    top: 48px;
    color: var(--white);
  }
  .contact-name {
    font-weight: 700;
    font-size: 27px;
    margin: 0;
  }
  .contact-title {
    font-weight: 400;
    font-size: 15px;
    margin: 6px 0 32px;
  }
  .contact-list {
    list-style: none;
    margin: 0;
    padding: 0;
    font-size: 15px;
  }
  .contact-list li {
    display: flex;
    align-items: center;
    gap: 10px;
    margin-bottom: 8px;
  }
  .contact-list svg { width: 14px; height: 14px; flex: none; }
  .contact-address {
    font-size: 15px;
    line-height: 1.45;
    margin: 14px 0 0;
  }
  .card-back .wordmark {
    position: absolute;
    left: 370px;
    right: 30px;
    top: 120px;
    flex-direction: column;
    gap: 14px;
    font-size: 40px;
    text-align: center;
    color: var(--teal);
  }
  .card-back .wordmark-name { display: block; }
  .card-back .wordmark-mark {
    width: 40px;
    height: 40px;
    border-radius: 8px;
    background: var(--teal);
  }
</style>
</head>
<body>
<main class="stage">
  <section class="card card-front">
    <div class="wordmark">
      <span class="wordmark-mark"></span>
      <span class="wordmark-name">Brivora Collective</span>
    </div>
  </section>

  <section class="card card-back">
    <svg class="curve" viewBox="0 0 700 400" preserveAspectRatio="none">
      <defs>
        <linearGradient id="backTeal" x1="0" y1="0" x2="1" y2="1">
          <stop offset="0" stop-color="#007a70"/>
          <stop offset="1" stop-color="#00564e"/>
        </linearGradient>
      </defs>
      <path d="M0 0 H470 C380 60 330 220 320 400 H0 Z" fill="url(#backTeal)"/>
      <path d="M445 0 C355 60 305 220 295 400" fill="none" stroke="#ffffff" stroke-width="4"/>
      <path d="M458 0 C368 60 318 220 308 400" fill="none" stroke="#ffffff" stroke-width="4"/>
    </svg>

    <div class="contact">
      <h1 class="contact-name">Marcus Delane</h1>
      <p class="contact-title">Founder &amp; Director</p>
      <ul class="contact-list">
        <li>
          <svg viewBox="0 0 24 24"><path fill="#fff" d="M6.6 10.8a15.2 15.2 0 0 0 6.6 6.6l2.2-2.2a1 1 0 0 1 1-.25 11.4 11.4 0 0 0 3.6.57 1 1 0 0 1 1 1V20a1 1 0 0 1-1 1A17 17 0 0 1 3 4a1 1 0 0 1 1-1h3.5a1 1 0 0 1 1 1c0 1.25.2 2.45.57 3.57a1 1 0 0 1-.25 1z"/></svg>
          (555)-204-7316
        </li>
        <li>
          <svg viewBox="0 0 24 24"><path fill="#fff" d="M2 5h20v14H2z"/><path d="M2 5l10 8 10-8" fill="none" stroke="#00695f" stroke-width="2"/></svg>
          delane@brivoracollective.com
        </li>
        <li>
          <svg viewBox="0 0 24 24"><circle cx="12" cy="12" r="10" fill="#fff"/><path d="M2 12h20M12 2c3 3 3 17 0 20M12 2c-3 3-3 17 0 20" fill="none" stroke="#00695f" stroke-width="1.6"/></svg>
          www.brivoracollective.com
        </li>
      </ul>
      <p class="contact-address">4170 Alder Lane<br>Cedar Falls Oregon 97310</p>
    </div>

    <div class="wordmark">
      <span class="wordmark-mark"></span>
      <span class="wordmark-name">Brivora<br>Collective</span>
    </div>
  </section>
</main>
</body>
</html>
```